Infographics and Charts Design

Need to create professional and simple Infographics, charts based on attached. Need in SVG, PDF and PNG formats with editable version included

Need a NEW design based on data/content in file Tallow QJ ROI v5 and Sample design

Target Market(s)

Network Security, Technology, Contact Center

Industry/Entity Type

Information Technology

Colors

Designer to choose colors to be used in the design.

Requirements
Must have
• Highly professional, Technology oriented and simple/elegant design. Must have white base color covering 70% of the design. Must be of very high quality that look great on website and in PDFs.
Should not have
• No Red, Yellow, Green or other dark colors

```html
<!DOCTYPE html>
<html lang="en">
<head>
<meta charset="utf-8">
<title>Tallow QJ – Security ROI Infographic</title>
<link rel="stylesheet" href="https://fonts.googleapis.com/css2?family=Roboto:wght@400;500;700;900&display=swap">
<style>
  :root{
    --page:#ffffff;
    --panel:#ececec;
    --frame:#9a9a9a;
    --blue:#2a9fd8;
    --blue-deep:#1b85c6;
    --slate:#86a6d4;
    --teal:#27b89c;
    --teal-title:#1eab97;
    --sky:#35a8dc;
    --line:#2a8fc8;
    --dot-line:#8cc2e2;
    --ink:#3a3a3a;
    --map:#dfe2e5;
  }
  html,body{margin:0;padding:0;width:1200px;height:462px;overflow:hidden;background:var(--page);}
  .canvas{display:block;width:1200px;height:462px;font-family:"Roboto",Arial,sans-serif;}
  .frame{fill:none;stroke:var(--frame);stroke-width:1.5;}
  .panel{fill:var(--panel);}
  .title{font-family:"Roboto",Arial,sans-serif;font-weight:700;font-size:38px;fill:var(--teal-title);text-anchor:middle;letter-spacing:.5px;}
  .subtitle{font-size:16px;fill:var(--ink);text-anchor:middle;}
  .title-bar{stroke:var(--blue);stroke-width:3;}
  .tag rect{fill:#fff;}
  .tag text{font-size:13px;font-weight:700;fill:var(--blue-deep);text-anchor:middle;letter-spacing:.3px;}
  .trend{fill:none;stroke:var(--blue);stroke-width:2.5;stroke-linejoin:round;stroke-linecap:round;}
  .map{fill:var(--map);}
  .row rect{rx:9;}
  .row text{font-size:13.5px;font-weight:500;fill:#fff;text-anchor:middle;}
  .row .ring{fill:#fff;}
  .row .num{font-size:15px;font-weight:400;}
  .c1 rect,.c1 .dot{fill:var(--blue);}
  .c2 rect,.c2 .dot{fill:var(--slate);}
  .c3 rect,.c3 .dot{fill:var(--teal);}
  .c4 rect,.c4 .dot{fill:var(--blue-deep);}
  .link{stroke:var(--dot-line);stroke-width:1.4;stroke-dasharray:3 3;fill:none;}
  .connector{stroke:var(--line);stroke-width:1.6;fill:none;}
  .hub .halo{fill:#fff;stroke:#b9dcef;stroke-width:2;}
  .hub text{font-size:15px;font-weight:700;fill:#fff;text-anchor:middle;}
  .hub.blue .core{fill:var(--blue);}
  .hub.teal .core{fill:var(--teal);}
  .disc-halo{fill:#fff;stroke:#d6e9f3;stroke-width:2;}
  .wedge-top{fill:var(--teal);}
  .wedge-left{fill:var(--blue-deep);}
  .wedge-right{fill:var(--sky);}
  .wedge-gap{stroke:#fff;stroke-width:7;fill:none;}
  .disc-label{font-size:13px;fill:#fff;}
  .brand-mark{fill:#fff;}
  .icon{fill:#fff;}
  .icon-line{fill:none;stroke:#fff;stroke-width:4;stroke-linecap:round;}
  .note{font-size:14px;font-weight:500;fill:var(--ink);text-anchor:middle;}
  .result rect{rx:4;}
  .result.blue rect{fill:var(--blue);}
  .result.teal rect{fill:var(--teal);}
  .result text{font-size:19px;fill:#fff;text-anchor:middle;}
  .result tspan.strong{font-weight:700;}
  .footer-line{stroke:#8fcbe6;stroke-width:1.2;stroke-dasharray:2 3;}
  .footer-text{font-size:15px;fill:var(--blue);}
</style>
</head>
<body>
<svg class="canvas" viewBox="0 0 2576 992" xmlns="http://www.w3.org/2000/svg">
  <rect class="frame" x="61" y="60" width="2447" height="864"/>
  <line class="frame" x1="1284" y1="60" x2="1284" y2="924"/>

  <!-- ===== Page 1: Contact Center Agents ===== -->
  <g class="sheet contact-center">
    <rect class="panel" x="77" y="80" width="1191" height="824"/>
    <rect class="map" role="img" aria-label="Dotted world map backdrop" x="462" y="210" width="378" height="195" rx="40"/>

    <line class="title-bar" x1="425" y1="136" x2="425" y2="190"/>
    <line class="title-bar" x1="920" y1="136" x2="920" y2="190"/>
    <text class="title" x="672" y="167">CONTACT CENTER AGENTS</text>
    <text class="subtitle" x="672" y="186">Availability, Time, CSAT, Data Protection, CLV, Sales Conversion</text>

    <g class="trend-icon down">
      <path class="trend" d="M186 194H274M198 192V150h8v42M214 192V138h8v54M230 192V160h8v32M246 192V176h8v16M212 134l26 24 18-4 14 14M262 166l8 2-2-8"/>
    </g>
    <g class="tag"><rect x="165" y="204" width="125" height="24"/><text x="227" y="221">NEGATIVE IMPACT</text></g>
    <g class="trend-icon up">
      <path class="trend" d="M1088 194H1150M1090 192V176h8v16M1104 192V170h8v22M1118 192V160h8v32M1132 192V150h8v42M1088 170c30-6 44-20 56-32M1136 138h10v10"/>
    </g>
    <g class="tag"><rect x="1058" y="204" width="120" height="24"/><text x="1118" y="221">IMPROVEMENT</text></g>

    <!-- left connectors -->
    <g>
      <path class="connector" d="M443 341H490V745H443M490 543H540"/>
      <path class="link" d="M288 271L393 341M288 319L393 341M288 366L393 341M288 414L393 341"/>
      <path class="link" d="M288 473L393 543M288 520L393 543M288 567L393 543M288 615L393 543"/>
      <path class="link" d="M288 674L393 745M288 721L393 745M288 769L393 745M288 817L393 745"/>
    </g>

    <!-- left rows -->
    <g class="row c1" transform="translate(167 271)"><rect y="-21" width="126" height="42"/><text x="55" y="-2">Informational</text><text x="55" y="14">20%</text><circle class="ring" cx="121" r="17"/><circle class="dot" cx="121" r="13"/><text class="num" x="121" y="5">1</text></g>
    <g class="row c2" transform="translate(167 319)"><rect y="-21" width="126" height="42"/><text x="55" y="-2">Support</text><text x="55" y="14">45%</text><circle class="ring" cx="121" r="17"/><circle class="dot" cx="121" r="13"/><text class="num" x="121" y="5">2</text></g>
    <g class="row c3" transform="translate(167 366)"><rect y="-21" width="126" height="42"/><text x="55" y="-2">Sale</text><text x="55" y="14">70%</text><circle class="ring" cx="121" r="17"/><circle class="dot" cx="121" r="13"/><text class="num" x="121" y="5">3</text></g>
    <g class="row c4" transform="translate(167 414)"><rect y="-21" width="126" height="42"/><text x="55" y="-2">Emergency</text><text x="55" y="14">Catastrophic</text><circle class="ring" cx="121" r="17"/><circle class="dot" cx="121" r="13"/><text class="num" x="121" y="5">4</text></g>

    <g class="row c1" transform="translate(167 473)"><rect y="-21" width="126" height="42"/><text x="55" y="-2">Informational</text><text x="55" y="14">5%</text><circle class="ring" cx="121" r="17"/><circle class="dot" cx="121" r="13"/><text class="num" x="121" y="5">1</text></g>
    <g class="row c2" transform="translate(167 520)"><rect y="-21" width="126" height="42"/><text x="55" y="-2">Support</text><text x="55" y="14">35%</text><circle class="ring" cx="121" r="17"/><circle class="dot" cx="121" r="13"/><text class="num" x="121" y="5">2</text></g>
    <g class="row c3" transform="translate(167 567)"><rect y="-21" width="126" height="42"/><text x="55" y="-2">Sale</text><text x="55" y="14">85%</text><circle class="ring" cx="121" r="17"/><circle class="dot" cx="121" r="13"/><text class="num" x="121" y="5">3</text></g>
    <g class="row c4" transform="translate(167 615)"><rect y="-21" width="126" height="42"/><text x="55" y="-2">Emergency</text><text x="55" y="14">90%</text><circle class="ring" cx="121" r="17"/><circle class="dot" cx="121" r="13"/><text class="num" x="121" y="5">4</text></g>

    <g class="row c1" transform="translate(167 674)"><rect y="-21" width="126" height="42"/><text x="55" y="-2">Informational</text><text x="55" y="14">35%</text><circle class="ring" cx="121" r="17"/><circle class="dot" cx="121" r="13"/><text class="num" x="121" y="5">1</text></g>
    <g class="row c2" transform="translate(167 721)"><rect y="-21" width="126" height="42"/><text x="55" y="-2">Support</text><text x="55" y="14">65%</text><circle class="ring" cx="121" r="17"/><circle class="dot" cx="121" r="13"/><text class="num" x="121" y="5">2</text></g>
    <g class="row c3" transform="translate(167 769)"><rect y="-21" width="126" height="42"/><text x="55" y="-2">Sale</text><text x="55" y="14">70%</text><circle class="ring" cx="121" r="17"/><circle class="dot" cx="121" r="13"/><text class="num" x="121" y="5">3</text></g>
    <g class="row c4" transform="translate(167 817)"><rect y="-21" width="126" height="42"/><text x="55" y="-2">Emergency</text><text x="55" y="14">80%</text><circle class="ring" cx="121" r="17"/><circle class="dot" cx="121" r="13"/><text class="num" x="121" y="5">4</text></g>

    <g class="hub blue" transform="translate(393 341)"><circle class="halo" r="52"/><circle class="core" r="43"/><text y="5">Availability</text></g>
    <g class="hub teal" transform="translate(393 543)"><circle class="halo" r="52"/><circle class="core" r="43"/><text y="-2">Wait</text><text y="14">Time</text></g>
    <g class="hub blue" transform="translate(393 745)"><circle class="halo" r="52"/><circle class="core" r="43"/><text y="-2">CSAT</text><text y="14">Impact</text></g>

    <!-- center disc -->
    <g class="disc" transform="translate(672 543)">
      <circle class="disc-halo" r="138"/>
      <path class="wedge-top" d="M0 0L-59 -102A118 118 0 0 1 59 -102Z"/>
      <path class="wedge-left" d="M0 0L0 118A118 118 0 0 1 -59 -102Z"/>
      <path class="wedge-right" d="M0 0L59 -102A118 118 0 0 1 0 118Z"/>
      <path class="wedge-gap" d="M0 0L-62 -107M0 0L62 -107M0 0V122"/>
      <g class="phone-icon">
        <path class="icon-line" d="M-22 -88c-4 6 2 20 12 30s22 14 28 10l-8-8-6 4c-6-2-14-10-16-16l4-6z"/>
        <rect class="icon" x="-2" y="-98" width="30" height="22" rx="11"/>
        <path class="icon" d="M2 -80l-6 8 12-4z"/>
      </g>
      <g class="lock-icon">
        <path class="icon-line" d="M-70 -2v-12a13 13 0 0 1 26 0v12"/>
        <rect class="icon" x="-80" y="-4" width="46" height="38" rx="4"/>
        <circle fill="var(--blue-deep)" cx="-57" cy="12" r="5"/>
        <rect fill="var(--blue-deep)" x="-59" y="14" width="4" height="10"/>
      </g>
      <text class="disc-label" x="-50" y="69" text-anchor="middle">Traditional</text>
      <text class="disc-label" x="-43" y="82" text-anchor="middle">Security</text>
      <rect class="brand-mark" x="36" y="-6" width="22" height="22"/>
      <text class="disc-label" x="18" y="69">Tallow QJ</text>
      <text class="disc-label" x="18" y="82">Advantage</text>
    </g>

    <!-- right connectors -->
    <g>
      <path class="connector" d="M903 341H856V745H903M856 543H808"/>
      <path class="link" d="M1058 271L953 341M1058 319L953 341M1058 366L953 341M1058 414L953 341"/>
      <path class="link" d="M1058 473L953 543M1058 520L953 543M1058 567L953 543M1058 615L953 543"/>
      <path class="link" d="M1058 674L953 745M1058 721L953 745M1058 769L953 745M1058 817L953 745"/>
    </g>

    <g class="row c1" transform="translate(1058 271)"><rect x="-2" y="-21" width="122" height="42"/><text x="64" y="-2">Informational</text><text x="64" y="14">&gt;95%</text><circle class="ring" r="17"/><circle class="dot" r="13"/><text class="num" y="5">1</text></g>
    <g class="row c2" transform="translate(1058 319)"><rect x="-2" y="-21" width="122" height="42"/><text x="64" y="-2">Support</text><text x="64" y="14">&gt;95%</text><circle class="ring" r="17"/><circle class="dot" r="13"/><text class="num" y="5">2</text></g>
    <g class="row c3" transform="translate(1058 366)"><rect x="-2" y="-21" width="122" height="42"/><text x="64" y="-2">Sale</text><text x="64" y="14">&gt;98%</text><circle class="ring" r="17"/><circle class="dot" r="13"/><text class="num" y="5">3</text></g>
    <g class="row c4" transform="translate(1058 414)"><rect x="-2" y="-21" width="122" height="42"/><text x="64" y="-2">Emergency</text><text x="64" y="14">&gt;99%</text><circle class="ring" r="17"/><circle class="dot" r="13"/><text class="num" y="5">4</text></g>

    <g class="row c1" transform="translate(1058 473)"><rect x="-2" y="-21" width="122" height="42"/><text x="64" y="-2">Informational</text><text x="64" y="14">5%</text><circle class="ring" r="17"/><circle class="dot" r="13"/><text class="num" y="5">1</text></g>
    <g class="row c2" transform="translate(1058 520)"><rect x="-2" y="-21" width="122" height="42"/><text x="64" y="-2">Support</text><text x="64" y="14">5%</text><circle class="ring" r="17"/><circle class="dot" r="13"/><text class="num" y="5">2</text></g>
    <g class="row c3" transform="translate(1058 567)"><rect x="-2" y="-21" width="122" height="42"/><text x="64" y="-2">Sale</text><text x="64" y="14">10%</text><circle class="ring" r="17"/><circle class="dot" r="13"/><text class="num" y="5">3</text></g>
    <g class="row c4" transform="translate(1058 615)"><rect x="-2" y="-21" width="122" height="42"/><text x="64" y="-2">Emergency</text><text x="64" y="14">10%</text><circle class="ring" r="17"/><circle class="dot" r="13"/><text class="num" y="5">4</text></g>

    <g class="row c1" transform="translate(1058 674)"><rect x="-2" y="-21" width="122" height="42"/><text x="64" y="-2">Informational</text><text x="64" y="14">0%</text><circle class="ring" r="17"/><circle class="dot" r="13"/><text class="num" y="5">1</text></g>
    <g class="row c2" transform="translate(1058 721)"><rect x="-2" y="-21" width="122" height="42"/><text x="64" y="-2">Support</text><text x="64" y="14">10%</text><circle class="ring" r="17"/><circle class="dot" r="13"/><text class="num" y="5">2</text></g>
    <g class="row c3" transform="translate(1058 769)"><rect x="-2" y="-21" width="122" height="42"/><text x="64" y="-2">Sale</text><text x="64" y="14">10%</text><circle class="ring" r="17"/><circle class="dot" r="13"/><text class="num" y="5">3</text></g>
    <g class="row c4" transform="translate(1058 817)"><rect x="-2" y="-21" width="122" height="42"/><text x="64" y="-2">Emergency</text><text x="64" y="14">5%</text><circle class="ring" r="17"/><circle class="dot" r="13"/><text class="num" y="5">4</text></g>

    <g class="hub blue" transform="translate(953 341)"><circle class="halo" r="52"/><circle class="core" r="43"/><text y="5">Availability</text></g>
    <g class="hub teal" transform="translate(953 543)"><circle class="halo" r="52"/><circle class="core" r="43"/><text y="-2">Wait</text><text y="14">Time</text></g>
    <g class="hub blue" transform="translate(953 745)"><circle class="halo" r="52"/><circle class="core" r="43"/><text y="-2">CSAT</text><text y="14">Impact</text></g>

    <text class="note" x="952" y="627">80-85%</text>
    <text class="note" x="952" y="643">Improvement</text>
    <text class="note" x="952" y="659">Across the</text>
    <text class="note" x="952" y="675">Board</text>

    <text class="footer-text" x="105" y="879">Page</text>
    <line class="footer-line" x1="148" y1="877" x2="1228" y2="877"/>
    <text class="footer-text" x="1234" y="879">1</text>
  </g>

  <!-- ===== Page 2: Collaboration / Back Office User ===== -->
  <g class="sheet back-office">
    <rect class="panel" x="1300" y="80" width="1191" height="824"/>
    <rect class="map" role="img" aria-label="Dotted world map backdrop" x="1686" y="210" width="378" height="195" rx="40"/>

    <line class="title-bar" x1="1565" y1="136" x2="1565" y2="190"/>
    <line class="title-bar" x1="2228" y1="136" x2="2228" y2="190"/>
    <text class="title" x="1896" y="167">COLLABORATION/BACK OFFICE USER</text>
    <text class="subtitle" x="1896" y="186">Security, Adoption, Productivity</text>

    <g class="trend-icon down">
      <path class="trend" d="M1410 229H1498M1422 227V185h8v42M1438 227V173h8v54M1454 227V195h8v32M1470 227V211h8v16M1436 169l26 24 18-4 14 14M1486 201l8 2-2-8"/>
    </g>
    <g class="tag"><rect x="1390" y="239" width="123" height="24"/><text x="1451" y="256">NEGATIVE IMPACT</text></g>
    <g class="trend-icon up">
      <path class="trend" d="M2312 229H2374M2314 227V211h8v16M2328 227V205h8v22M2342 227V195h8v32M2356 227V185h8v42M2312 205c30-6 44-20 56-32M2360 173h10v10"/>
    </g>
    <g class="tag"><rect x="2283" y="239" width="120" height="24"/><text x="2343" y="256">IMPROVEMENT</text></g>

    <g>
      <path class="connector" d="M1665 383H1715L1770 530M1665 584H1760M1665 787H1715L1770 640"/>
      <path class="connector" d="M2125 383H2078L2022 530M2032 584H2125M2125 787H2078L2022 640"/>
      <path class="link" d="M1512 312L1615 383M1512 360L1615 383M1512 407L1615 383M1512 455L1615 383"/>
      <path class="link" d="M1512 514L1615 584M1512 561L1615 584M1512 608L1615 584M1512 656L1615 584"/>
      <path class="link" d="M1512 763L1615 787M1512 810L1615 787"/>
      <path class="link" d="M2227 380H2280M2227 584H2280M2227 787H2255"/>
    </g>

    <g class="row c1" transform="translate(1390 312)"><rect y="-21" width="126" height="42"/><text x="55" y="-2">Informational</text><text x="55" y="14">10%</text><circle class="ring" cx="121" r="17"/><circle class="dot" cx="121" r="13"/><text class="num" x="121" y="5">1</text></g>
    <g class="row c2" transform="translate(1390 360)"><rect y="-21" width="126" height="42"/><text x="55" y="-2">Sale</text><text x="55" y="14">40%</text><circle class="ring" cx="121" r="17"/><circle class="dot" cx="121" r="13"/><text class="num" x="121" y="5">2</text></g>
    <g class="row c3" transform="translate(1390 407)"><rect y="-21" width="126" height="42"/><text x="55" y="-2">Regulated</text><text x="55" y="14">90%</text><circle class="ring" cx="121" r="17"/><circle class="dot" cx="121" r="13"/><text class="num" x="121" y="5">3</text></g>
    <g class="row c4" transform="translate(1390 455)"><rect y="-21" width="126" height="42"/><text x="55" y="-2">Non-Regulated</text><text x="55" y="14">30%</text><circle class="ring" cx="121" r="17"/><circle class="dot" cx="121" r="13"/><text class="num" x="121" y="5">4</text></g>

    <g class="row c1" transform="translate(1390 514)"><rect y="-21" width="126" height="42"/><text x="55" y="-2">Informational</text><text x="55" y="14">60%</text><circle class="ring" cx="121" r="17"/><circle class="dot" cx="121" r="13"/><text class="num" x="121" y="5">1</text></g>
    <g class="row c2" transform="translate(1390 561)"><rect y="-21" width="126" height="42"/><text x="55" y="-2">Sale</text><text x="55" y="14">70%</text><circle class="ring" cx="121" r="17"/><circle class="dot" cx="121" r="13"/><text class="num" x="121" y="5">2</text></g>
    <g class="row c3" transform="translate(1390 608)"><rect y="-21" width="126" height="42"/><text x="55" y="-2">Regulated</text><text x="55" y="14">100%</text><circle class="ring" cx="121" r="17"/><circle class="dot" cx="121" r="13"/><text class="num" x="121" y="5">3</text></g>
    <g class="row c4" transform="translate(1390 656)"><rect y="-21" width="126" height="42"/><text x="55" y="-2">Non-Regulated</text><text x="55" y="14">65%</text><circle class="ring" cx="121" r="17"/><circle class="dot" cx="121" r="13"/><text class="num" x="121" y="5">4</text></g>

    <g class="row c1" transform="translate(1390 763)"><rect y="-21" width="126" height="42"/><text x="55" y="-2">Internal</text><text x="55" y="14">80%</text><circle class="ring" cx="121" r="17"/><circle class="dot" cx="121" r="13"/><text class="num" x="121" y="5">1</text></g>
    <g class="row c2" transform="translate(1390 810)"><rect y="-21" width="126" height="42"/><text x="55" y="-2">Customer Facing</text><text x="55" y="14">10%</text><circle class="ring" cx="121" r="17"/><circle class="dot" cx="121" r="13"/><text class="num" x="121" y="5">2</text></g>

    <g class="hub blue" transform="translate(1615 383)"><circle class="halo" r="52"/><circle class="core" r="43"/><text y="5">Security</text></g>
    <g class="hub teal" transform="translate(1615 584)"><circle class="halo" r="52"/><circle class="core" r="43"/><text y="5">Productivity</text></g>
    <g class="hub blue" transform="translate(1615 787)"><circle class="halo" r="52"/><circle class="core" r="43"/><text y="5">Adoption</text></g>

    <g class="disc" transform="translate(1896 584)">
      <circle class="disc-halo" r="138"/>
      <path class="wedge-top" d="M0 0L-59 -102A118 118 0 0 1 59 -102Z"/>
      <path class="wedge-left" d="M0 0L0 118A118 118 0 0 1 -59 -102Z"/>
      <path class="wedge-right" d="M0 0L59 -102A118 118 0 0 1 0 118Z"/>
      <path class="wedge-gap" d="M0 0L-62 -107M0 0L62 -107M0 0V122"/>
      <g class="signal-icon">
        <circle class="icon" cx="0" cy="-72" r="6"/>
        <path class="icon-line" d="M-12 -84a17 17 0 0 1 24 0M-20 -92a28 28 0 0 1 40 0M0 -66V-52M-14 -52h28"/>
      </g>
      <g class="lock-icon">
        <path class="icon-line" d="M-70 -2v-12a13 13 0 0 1 26 0v12"/>
        <rect class="icon" x="-80" y="-4" width="46" height="38" rx="4"/>
        <circle fill="var(--blue-deep)" cx="-57" cy="12" r="5"/>
        <rect fill="var(--blue-deep)" x="-59" y="14" width="4" height="10"/>
      </g>
      <text class="disc-label" x="-50" y="68" text-anchor="middle">Traditional</text>
      <text class="disc-label" x="-43" y="81" text-anchor="middle">Security</text>
      <rect class="brand-mark" x="36" y="-6" width="22" height="22"/>
      <text class="disc-label" x="18" y="68">Tallow QJ</text>
      <text class="disc-label" x="18" y="81">Advantage</text>
    </g>

    <g class="hub blue" transform="translate(2175 383)"><circle class="halo" r="52"/><circle class="core" r="43"/><text y="5">Security</text></g>
    <g class="hub teal" transform="translate(2175 584)"><circle class="halo" r="52"/><circle class="core" r="43"/><text y="5">Productivity</text></g>
    <g class="hub blue" transform="translate(2175 787)"><circle class="halo" r="52"/><circle class="core" r="43"/><text y="5">Adoption</text></g>

    <g class="result blue"><rect x="2280" y="360" width="122" height="42"/><text x="2341" y="388">Over <tspan class="strong">95%</tspan></text></g>
    <g class="result teal"><rect x="2280" y="563" width="122" height="42"/><text x="2341" y="591">Over <tspan class="strong">80%</tspan></text></g>
    <g class="result blue"><rect x="2255" y="766" width="147" height="42"/><text x="2328" y="794">Retain Over <tspan class="strong">90%</tspan></text></g>

    <text class="footer-text" x="1328" y="879">Page</text>
    <line class="footer-line" x1="1370" y1="877" x2="2450" y2="877"/>
    <text class="footer-text" x="2455" y="879">2</text>
  </g>
</svg>
</body>
</html>
```